Ledgerforge Studio - WordPress Theme & Logo

Design a logo and Wordpress website design for Ledgerforge Studio. Ledgerforge Studio provides cryptocurrency development services to clients who need a team to create & continue developing a new cryptocurrency or who want to replace their current cryptocurrency development team. more details in the attached document.
Updates

Target Market(s)

Entrepreneurs who are building a business / platform that makes use of an underlying cryptocurrency.

Logo Text

LS or Ledgerforge Studio

Coding

Coded - Design and coding required

Font styles to use
Sans Serif

Requirements
Must have
• Professional logo, complete coded Wordpress theme for all pages, containing all specified links and buttons
Nice to have
• It would be nice if the buttons that are meant to integrate with Dealcurrent contain the necessary code for that. I can provide any necessary Dealcurrent details from my account.
Should not have
• Slow loading time

```html
<!DOCTYPE html>
<html lang="en">
<head>
<meta charset="UTF-8">
<title>Ledgerforge Studio</title>
<link href="https://fonts.googleapis.com/css2?family=Poppins:wght@400;600;700&family=Roboto:wght@400;500;700&display=swap" rel="stylesheet">
<style>
:root{
  --purple:#8a2a9c;
  --blue:#1c7fd1;
  --grad:linear-gradient(90deg,#8a2a9c,#1c7fd1);
  --ink:#111;
  --text:#555;
  --hero-bg:#f3f8fe;
  --soft:#f4f4f6;
  --white:#fff;
  --star:#f5c518;
}
*{box-sizing:border-box;margin:0;padding:0}
html,body{width:1200px;height:3609px;overflow:hidden}
body{font-family:'Roboto',sans-serif;color:var(--text);background:var(--white);position:relative}
section,header,footer{position:absolute;left:0;width:1200px}
.abs{position:absolute}
.title{font-family:'Poppins',sans-serif;color:var(--ink);font-weight:400;text-align:center}
.title b{font-weight:700}
.btn{display:inline-flex;align-items:center;gap:8px;background:var(--grad);color:#fff;font-family:'Roboto',sans-serif;font-weight:500;border-radius:22px;text-decoration:none}
.btn .dot{width:13px;height:13px;border-radius:50%;background:#fff;display:inline-block;position:relative}
.btn .dot::after{content:"";position:absolute;left:3px;top:3.5px;border-left:6px solid var(--purple);border-top:3px solid transparent;border-bottom:3px solid transparent}

/* header */
.site-header{top:0;height:98px;background:var(--hero-bg)}
.brand{left:68px;top:24px;display:flex;align-items:center;gap:12px}
.brand-mark{width:48px;height:48px;border-radius:50%;background:var(--purple)}
.brand-name{font-family:'Poppins',sans-serif;font-weight:600;font-size:20px;color:#222}
.nav{left:344px;top:38px;display:flex;gap:23px;font-size:15px;color:#222;font-weight:500}
.nav .active{color:var(--blue)}
.nav-cta{left:891px;top:29px;padding:10px 19px;font-size:16px}

/* hero */
.hero{top:98px;height:718px;background:var(--hero-bg)}
.hero h1{position:absolute;top:58px;width:100%;font-size:38px;line-height:46px}
.hero p{position:absolute;top:172px;left:210px;width:780px;text-align:center;font-size:15px;line-height:27.5px;color:#222}
.hero .btn{position:absolute;left:471px;top:278px;padding:10px 18px;font-size:15px}
.hero-wave{position:absolute;left:0;top:322px;width:1200px;height:396px;
  background:linear-gradient(100deg,rgba(60,130,210,.55) 0%,rgba(90,120,210,.35) 45%,rgba(150,60,170,.5) 75%,rgba(160,80,180,.3) 100%);
  clip-path:polygon(0 40%,20% 25%,45% 5%,60% 0,75% 15%,100% 10%,100% 100%,0 100%)}

/* why */
.why{top:816px;height:556px;background:linear-gradient(180deg,#fff,#f7f7f9)}
.why h2{position:absolute;top:82px;width:100%;font-size:36px}
.hex{position:absolute;top:178px;width:252px;height:287px;filter:drop-shadow(0 8px 14px rgba(0,0,0,.1))}
.hex-body{width:100%;height:100%;background:#fff;clip-path:polygon(50% 0,100% 25%,100% 75%,50% 100%,0 75%,0 25%)}
.hex-top{position:absolute;left:44px;top:0;width:164px;height:94px;background:var(--grad);clip-path:polygon(50% 0,100% 50%,50% 100%,0 50%)}
.hex h3{position:absolute;top:126px;width:100%;text-align:center;font-size:20px;font-weight:500;color:#111}
.hex p{position:absolute;top:158px;left:10px;right:10px;text-align:center;font-size:14px;line-height:24px;color:#666}

/* who */
.who{top:1372px;height:395px;background:var(--soft)}
.who-photo{position:absolute;left:0;top:0;width:588px;height:395px;background:linear-gradient(135deg,#d9dde3,#9aa3ad 55%,#4a4f57)}
.who h2{position:absolute;left:642px;top:56px;font-size:38px;text-align:left}
.who p{position:absolute;left:642px;top:126px;width:460px;font-size:14px;line-height:26.5px;color:#666}
.who .btn{position:absolute;left:642px;top:286px;padding:14px 30px;font-size:15px;font-weight:700;border-radius:24px}

/* testimonials */
.clients{top:1767px;height:585px;background:#fff}
.clients h2{position:absolute;top:92px;width:100%;font-size:38px}
.tcard{position:absolute;top:222px;width:308px;height:188px;background:#fff;border-radius:10px;box-shadow:0 6px 18px rgba(0,0,0,.1);border-top:3px solid var(--purple)}
.tcard::after{content:"";position:absolute;left:147px;bottom:-8px;border-top:8px solid #fff;border-left:8px solid transparent;border-right:8px solid transparent}
.tcard p{position:absolute;top:66px;left:24px;right:24px;text-align:center;font-size:14px;line-height:25.5px;color:#555}
.avatar{position:absolute;left:110px;top:-46px;width:88px;height:88px;border-radius:50%;background:linear-gradient(160deg,#e6e6e6,#9a9a9a);border:3px solid #fff}
.tname{position:absolute;top:437px;width:308px;text-align:center;font-size:15px;color:#222;font-weight:500}
.tname small{font-size:10px;font-weight:400}
.stars{position:absolute;top:459px;width:308px;text-align:center;color:var(--star);font-size:13px;letter-spacing:1px}

/* services */
.services{top:2352px;height:890px;background:var(--soft)}
.services h2{position:absolute;top:54px;width:100%;font-size:38px}
.services .lead{position:absolute;left:128px;width:944px;text-align:center;font-size:14px;line-height:24px;color:#666}
.scard{position:absolute;top:276px;width:312px;height:403px;background:#fff;border-radius:8px;box-shadow:0 6px 18px rgba(0,0,0,.08)}
.scard .ph{position:absolute;left:5px;top:5px;width:302px;height:178px;border-radius:6px}
.scard h3{position:absolute;top:216px;width:100%;text-align:center;font-size:17px;font-weight:500;color:#111}
.scard p{position:absolute;top:254px;left:16px;right:16px;text-align:center;font-size:14px;line-height:25px;color:#666}
.arrow{position:absolute;top:462px;width:26px;height:42px}
.services .btn{position:absolute;left:471px;top:756px;padding:10px 18px;font-size:15px}

/* footer */
.site-footer{top:3242px;height:367px;background:linear-gradient(110deg,#7b2a9a 0%,#4b4aa8 50%,#1a7fce 100%);color:#fff}
.site-footer h4{position:absolute;top:92px;font-size:18px;font-weight:700}
.contact{position:absolute;left:110px;top:136px;width:250px;font-size:14px;line-height:20px}
.contact li{list-style:none;display:flex;gap:10px;margin-bottom:16px}
.contact svg{flex:none;margin-top:3px}
.links{position:absolute;top:140px;list-style:none;font-size:14px;line-height:26.5px}
.sub-form{position:absolute;left:714px;top:128px;width:240px;height:44px;border-radius:22px;background:#fff;font-size:11px;color:#888;padding:15px 22px}
.sub-btn{position:absolute;left:964px;top:128px;width:123px;height:44px;border-radius:22px;background:var(--purple);font-weight:700;font-size:16px;text-align:center;line-height:44px}
.consent{position:absolute;left:710px;top:200px;font-size:13px;font-weight:500}
.social{position:absolute;top:238px;width:32px;height:32px;border:1.5px solid #fff;border-radius:50%}
.copy{position:absolute;top:332px;width:100%;text-align:center;font-size:13px;border-top:1px solid rgba(255,255,255,.25);padding-top:14px;left:0}
.copy{top:318px;left:110px;width:980px}
</style>
</head>
<body>

<header class="site-header">
  <div class="abs brand"><span class="brand-mark"></span><span class="brand-name">Ledgerforge Studio</span></div>
  <nav class="abs nav"><span class="active">Home</span><span>About Us</span><span>Our Services</span><span>Service Tiers</span><span>Testimonials</span><span>Blog</span></nav>
  <a class="abs btn nav-cta">Schedule a Free Consultation</a>
</header>

<section class="hero">
  <h1 class="title"><b>Your own cryptocurrency. Secure,</b> easy to<br>use, &amp; built by an expert team.</h1>
  <p>Ledgerforge Studio adds professionalism to cryptocurrency development. Our done-for-you service covers everything from development and IT operations to ongoing support. You have access to a full team, for less than the typical cost of a single developer.</p>
  <a class="btn">Schedule a Free Consultation <span class="dot"></span></a>
  <div class="hero-wave" role="img" aria-label="Flowing dotted wave graphic in blue and purple"></div>
</section>

<section class="why">
  <h2 class="title"><b>Why choose</b> Ledgerforge Studio</h2>
  <div class="hex" style="left:175px"><div class="hex-body"></div><div class="hex-top"></div><h3>Value</h3><p>A team of experts, regular updates, and fixed costs</p></div>
  <div class="hex" style="left:474px"><div class="hex-body"></div><div class="hex-top"></div><h3>Support</h3><p>Receive advice and other services, beyond development.</p></div>
  <div class="hex" style="left:773px"><div class="hex-body"></div><div class="hex-top"></div><h3>Commitment</h3><p>Enjoy regular updates and new features.</p></div>
</section>

<section class="who">
  <div class="who-photo" role="img" aria-label="Photo of three colleagues working together at a laptop"></div>
  <h2 class="title"><b>Who</b> We Are</h2>
  <p>In addition to creating and enhancing cryptocurrencies for clients, the Ledgerforge Studio team has been running the Verant cryptocurrency since 2017. We prefer long-term relationships, enabling us to deliver the very highest quality and giving you peace of mind that you've got aprofessional and trustworthy team at your side.</p>
  <a class="btn">READ MORE <span class="dot"></span></a>
</section>

<section class="clients">
  <h2 class="title"><b>What Our</b> Clients Say</h2>
  <div class="tcard" style="left:112px"><div class="avatar" role="img" aria-label="Client portrait"></div><p>Sed ut perspiciatis unde omnis iste natus error sit voluptatem accusantium doloremque laudantium, totam rem aperiam, eaque ipsa</p></div>
  <div class="tname" style="left:112px">Nadia Ellery, <small>Chairman NVX</small></div><div class="stars" style="left:112px">★★★★★</div>
  <div class="tcard" style="left:446px"><div class="avatar" role="img" aria-label="Client portrait"></div><p>Sed ut perspiciatis unde omnis iste natus error sit voluptatem accusantium doloremque laudantium, totam rem aperiam, eaque ipsa</p></div>
  <div class="tname" style="left:446px">Lena Okafor, <small>Project Manager</small></div><div class="stars" style="left:446px">★★★★★</div>
  <div class="tcard" style="left:780px"><div class="avatar" role="img" aria-label="Client portrait"></div><p>Sed ut perspiciatis unde omnis iste natus error sit voluptatem accusantium doloremque laudantium, totam rem aperiam, eaque ipsa</p></div>
  <div class="tname" style="left:780px">Tomas Reyne, <small>Chairman NVX</small></div><div class="stars" style="left:780px">★★★★★</div>
</section>

<section class="services">
  <h2 class="title"><b>Our</b> Services</h2>
  <p class="lead" style="top:114px">Ledgerforge Studio provides a complete service that handles the development, IT operations and support for your cryptocurrency. Cryptocurrency development can be difficult and complex, and a quality development team is hard to find and expensive. expensive.</p>
  <p class="lead" style="top:176px">Ledgerforge Studio has an experienced team that has helped several clients launch and enhance their cryptocurrencies, including successfully running the Verant cryptocurrency since 2017, and writing a next-generation cryptocurrency from scratch.</p>
  <svg class="arrow" style="left:32px" viewBox="0 0 26 42"><polyline points="22,3 4,21 22,39" fill="none" stroke="#bbb" stroke-width="4"/></svg>
  <svg class="arrow" style="left:1132px" viewBox="0 0 26 42"><polyline points="4,3 22,21 4,39" fill="none" stroke="#bbb" stroke-width="4"/></svg>
  <div class="scard" style="left:108px"><div class="ph" role="img" aria-label="Photo of joined hands over a glowing digital globe" style="background:linear-gradient(135deg,#2a3550,#3d6fa8 50%,#1b2233)"></div><h3>Blockchain Creation &amp; Launch</h3><p>Base fixed price for cryptocurrency development &amp; launch--would be customizable based on client requirements</p></div>
  <div class="scard" style="left:444px"><div class="ph" role="img" aria-label="Photo of a laptop and tablet showing trading charts" style="background:linear-gradient(135deg,#e9dccb,#a7876a 55%,#5a4636)"></div><h3>Basic offering</h3><p>Lower cost per month<br>Slower release schedule<br>Client assists with testing new releases<br>Less input into future roadmap/features<br>Limited support hours/priority available</p></div>
  <div class="scard" style="left:780px"><div class="ph" role="img" aria-label="Photo of a business team meeting around a table" style="background:linear-gradient(135deg,#3a4150,#6d7688 55%,#b9b2a8)"></div><h3>Full service offering</h3><p>Mid-range cost per month<br>Releases every 1.5 - 2 months<br>Client can help request/prioritize new<br>Full testing by my team prior to release<br>Priority support during normal business</p></div>
  <a class="btn">Schedule a Free Consultation <span class="dot"></span></a>
</section>

<footer class="site-footer">
  <h4 style="left:110px">Contact Us</h4>
  <ul class="contact">
    <li><svg width="12" height="14" viewBox="0 0 12 14"><path d="M6 0a5 5 0 0 0-5 5c0 4 5 9 5 9s5-5 5-9a5 5 0 0 0-5-5z" fill="#4db2ff"/></svg><span>3501 Lorem ipsum dolor sit amet, consectetur</span></li>
    <li><svg width="14" height="12" viewBox="0 0 14 12"><rect width="14" height="11" rx="1" fill="#4db2ff"/></svg><span>info@ledgerforgestudio.example</span></li>
    <li><svg width="14" height="14" viewBox="0 0 14 14"><path d="M3 1l3 3-2 2a8 8 0 0 0 4 4l2-2 3 3-2 2C6 13 1 8 1 3z" fill="#4db2ff"/></svg><span>555.014.2290</span></li>
    <li><svg width="14" height="13" viewBox="0 0 14 13"><rect y="3" width="14" height="10" rx="2" fill="#4db2ff"/></svg><span>(555) 010 - 4477</span></li>
  </ul>
  <h4 style="left:394px">Links</h4>
  <ul class="links" style="left:395px"><li>Home</li><li>About Us</li><li>Our Services</li><li>Service Tiers</li><li>Testimonials</li></ul>
  <ul class="links" style="left:521px"><li>Terms &amp; Condition</li><li>Privacy Policy</li><li>Updates</li><li>Support</li><li>Contact</li></ul>
  <h4 style="left:710px">Subscribe for Updates</h4>
  <div class="sub-form">Emaill Address</div>
  <div class="sub-btn">SUBMIT</div>
  <div class="consent">☑&nbsp; Yes, Please Contact me.</div>
  <span class="social" style="left:710px"></span><span class="social" style="left:753px"></span><span class="social" style="left:796px"></span>
  <div class="copy">© 2021&nbsp; Ledgerforge Studio&nbsp; |&nbsp; All Rights Reserved</div>
</footer>

</body>
</html>
```